Brightway Talent Partners, LLC Business Card Design

Website URL: www.brightwaytalentpartners-example.com
I have attached a previous design that I find "okay" and adequate, but I wanted to explore some more distinctive/creative professional versions.
Our company provides business owners, executives and managers valuable information to help them make better people decisions. Our primary means of providing this information is through a comprehensive suite of employee assessment products across the employee life cycle that help clients better select, manage and retain talent. Company tagline is: Assess People, Predict Performance. Our employee assessment products fall into the following 3 categories:
- Assessments for Hiring Talent
- Assessments for Developing Talent
- Assessments for Retaining Talent
Please view our 3 minute overview video (link below) to get a sense of who we are:
http://videohost-example.com/q9Rt2LmXw8b
Our business personality is competent, modern, & friendly...driven by developing long lasting client relationships as opposed to one time customer transactions. We would like to see designs that are professional yet distinctive "cool business card!" and use primary logo colors/complementary color . Not sure if I prefer the gray font as shown in previous design or black...open to suggestions.
The final design should communicate competence, trust, and solutions. Also, I am an authorized business partner and consultant with two organizations that provide the assessment products I will market/use with clients. Attached are files for Meridale Worldwide and Tollard Worldwide that should be incorporated into the design (*very small but readable)

Industry/Entity Type
Business
Contact Information for Business Card
Dwight Halvers
Founder and Managing Partner
4381 North Juniper Mill Lane
Suite 715
Atlanta GA 30419-5183
Office: 555.014.2796
dhalvers@brightwaytalentpartners-example.com
www.brightwaytalentpartnrs-example.com

```html
<!DOCTYPE html>
<html lang="en">
<head>
<meta charset="utf-8">
<title>Brightway Talent Partners – Business Card</title>
<link rel="stylesheet" href="https://fonts.googleapis.com/css2?family=Open+Sans:wght@400;600;700&display=swap">
<style>
  :root {
    --page-bg: #e6e7e9;
    --navy: #2e2a78;
    --navy-light: #3b3690;
    --card-white: #ffffff;
    --accent-blue: #1f6fa8;
    --ink: #2a2a33;
    --icon: #2e2a78;
    --badge-fill: #d9dbe6;
    --hole: #9a9a9a;
    --globe-a: #7fb6e6;
    --globe-b: #1c4f93;
  }
  * { margin: 0; padding: 0; box-sizing: border-box; }
  html, body {
    width: 1200px; height: 720px; overflow: hidden;
    background: var(--page-bg);
    font-family: "Open Sans", Arial, sans-serif;
  }
  .card {
    position: absolute; left: 180px; top: 120px;
    width: 840px; height: 480px;
  }
  .card-shape { position: absolute; inset: 0; }
  .pill {
    position: absolute; left: 12px; width: 290px; height: 70px;
    background: var(--card-white); border-radius: 35px;
    display: flex; align-items: center; justify-content: center;
  }
  .pill--brand { top: 43px; flex-direction: column; }
  .pill--partner-a { top: 203px; }
  .pill--partner-b { top: 363px; }
  .brand-name {
    color: var(--navy); font-weight: 700; font-size: 19px;
    letter-spacing: -0.2px; white-space: nowrap;
  }
  .partner-badge {
    width: 210px; height: 36px; border-radius: 6px;
    background: var(--badge-fill);
  }
  .ornament {
    position: absolute; left: 536px; width: 44px; height: 28px;
    background: var(--navy); opacity: 0.85; border-radius: 3px;
  }
  .ornament--top { top: 40px; }
  .ornament--bottom { top: 408px; }
  .globe-emblem {
    position: absolute; left: 700px; top: 20px;
    width: 112px; height: 112px; border-radius: 50%;
    border: 6px solid var(--navy);
    background: radial-gradient(circle at 40% 35%, var(--globe-a), var(--globe-b));
  }
  .identity { position: absolute; left: 368px; top: 106px; }
  .identity__name {
    color: var(--accent-blue); font-weight: 700; font-size: 24px; line-height: 1.2;
  }
  .identity__title { color: var(--ink); font-size: 17px; line-height: 1.3; }
  .contact-list {
    position: absolute; left: 380px; top: 226px; list-style: none;
  }
  .contact-list li {
    display: flex; align-items: center; height: 38px;
    color: var(--ink); font-size: 17px; white-space: nowrap;
  }
  .contact-list svg { width: 16px; height: 16px; margin-right: 18px; flex: none; fill: var(--icon); }
  .card-hole {
    position: absolute; left: 798px; top: 224px;
    width: 28px; height: 28px; border-radius: 50%; background: var(--hole);
  }
</style>
</head>
<body>
  <div class="card">
    <svg class="card-shape" viewBox="0 0 840 480" aria-hidden="true">
      <rect width="840" height="480" fill="var(--navy)"/>
      <path d="M322 14 Q292 240 296 466 L300 466 Q300 240 330 14 Z" fill="var(--navy-light)"/>
      <path d="M330 14 L828 14 L828 466 L300 466 Q300 240 330 14 Z" fill="var(--card-white)"/>
    </svg>

    <div class="pill pill--brand"><span class="brand-name">Brightway Talent Partners</span></div>
    <div class="pill pill--partner-a"><div class="partner-badge" role="img" aria-label="Tollard Worldwide certified consultant badge"></div></div>
    <div class="pill pill--partner-b"><div class="partner-badge" role="img" aria-label="Meridale Worldwide authorized partner badge"></div></div>

    <div class="ornament ornament--top" role="img" aria-label="Decorative chevron mark"></div>
    <div class="ornament ornament--bottom" role="img" aria-label="Decorative chevron mark"></div>
    <div class="globe-emblem" role="img" aria-label="Globe illustration emblem"></div>

    <div class="identity">
      <p class="identity__name">Dwight Halvers</p>
      <p class="identity__title">Founder and Managing Partner</p>
    </div>

    <ul class="contact-list">
      <li><svg viewBox="0 0 24 24"><path d="M6.6 10.8a15 15 0 0 0 6.6 6.6l2.2-2.2a1 1 0 0 1 1-.25 11.4 11.4 0 0 0 3.6.57 1 1 0 0 1 1 1V20a1 1 0 0 1-1 1A17 17 0 0 1 3 4a1 1 0 0 1 1-1h3.5a1 1 0 0 1 1 1c0 1.25.2 2.45.57 3.57a1 1 0 0 1-.25 1z"/></svg>30419-5183</li>
      <li><svg viewBox="0 0 24 24"><path d="M12 2a10 10 0 1 0 0 20 10 10 0 0 0 0-20zm1 17.9V18h-2v1.9A8 8 0 0 1 4.1 13H6v-2H4.1A8 8 0 0 1 11 4.1V6h2V4.1A8 8 0 0 1 19.9 11H18v2h1.9a8 8 0 0 1-6.9 6.9z"/></svg>www.brightwaytalentpartnrs-example.com</li>
      <li><svg viewBox="0 0 24 24"><path d="M2 5h20v14H2zm2 2v.5l8 5 8-5V7z"/></svg>dhalvers@brightwaytalentpartners-example.com</li>
      <li><svg viewBox="0 0 24 24"><path d="M12 2a7 7 0 0 0-7 7c0 5 7 13 7 13s7-8 7-13a7 7 0 0 0-7-7zm0 9.5A2.5 2.5 0 1 1 12 6.5a2.5 2.5 0 0 1 0 5z"/></svg>4381 North Juniper Mill Lane Suite 715 Atlanta</li>
    </ul>

    <div class="card-hole"></div>
  </div>
</body>
</html>
```